7TrekZ 2019 driving event needs an event poster!

We need a poster design advertising our driving event next June. I would like to see a whole range of classic, modern, colourful, perhaps even cartoon or stylish designs using our logos and event details such as web address, social media handles, dates and locations.

As an event poster, it needs to be informative and eye catching. You are the designer, make it interesting!

We have added our 2019 logo in various colours, and the banner of our facebook page, consider 7trekz.com which is our website which has many event details and ideas.

Event is 4 days. We drive through 3 countries starting in London, travelling through Wales, the lakes and into Scotland, finishing in Edinburgh.

Other similar and popular driving events that might give some ideas are zephyr 5000, thunderline dash Europe, silverwind tour, etc

Colors

Designer to choose colors to be used in the design.

Requirements
Must have
• Eye-catching design. A cool look and feel. Perhaps a retro style. All ideas welcome.
Should not have
• A generic look and feel. Stolen images. Images I have to pay extra for. Something that looks like it took five minutes to slap together. No use of the word 'rally'. Its incredibly similar in all respects, but rally is a word that adds costs.

```html
<!DOCTYPE html>
<html lang="en">
<head>
<meta charset="utf-8">
<title>7TrekZ 2019 – Event Poster</title>
<link href="https://fonts.googleapis.com/css2?family=Archivo+Black&family=Cinzel:wght@700;900&family=Permanent+Marker&display=swap" rel="stylesheet">
<style>
  :root {
    --teal: #2b9fbb;
    --teal-dark: #1c7990;
    --teal-light: #4cb6cf;
    --ink: #17323b;
    --red: #e8231a;
    --band: rgba(225,228,230,0.75);
    --tab: #3c6470;
    --footer: #153c47;
    --white: #ffffff;
    --text: #151515;
  }
  * { margin: 0; padding: 0; box-sizing: border-box; }
  html, body { width: 1000px; height: 1200px; overflow: hidden; background: var(--white); }
  .poster {
    position: relative; width: 1000px; height: 1200px; overflow: hidden;
    background: linear-gradient(180deg, #e9ebec 0%, #ffffff 30%, #ffffff 100%);
    font-family: "Cinzel", serif; color: var(--text);
  }
  .road { position: absolute; inset: 0; width: 1000px; height: 1200px; }

  .brand-mark { position: absolute; left: 30px; top: 60px; width: 280px; height: 200px; display: flex; flex-direction: column; align-items: center; justify-content: center; gap: 10px; }
  .brand-mark .dot { width: 64px; height: 64px; border-radius: 50%; background: var(--teal); }
  .brand-mark .name { font-family: "Archivo Black", sans-serif; font-size: 56px; color: var(--teal-dark); line-height: 1; }

  .title {
    position: absolute; left: 330px; top: 108px; width: 660px; text-align: center; white-space: nowrap;
    font-family: "Archivo Black", sans-serif; font-size: 80px; line-height: 1;
    color: var(--teal); -webkit-text-stroke: 3px var(--ink); letter-spacing: 1px;
  }

  .stats, .countries {
    position: absolute; left: 0; width: 1000px; text-align: center; white-space: nowrap;
    font-family: "Permanent Marker", cursive; color: var(--teal-light);
    -webkit-text-stroke: 1.5px var(--ink); line-height: 1;
  }
  .stats { top: 290px; height: 66px; font-size: 54px; }
  .countries { top: 388px; height: 80px; font-size: 58px; display: flex; justify-content: center; align-items: flex-end; gap: 4px; }
  .countries .word { display: inline-block; }
  .flag { display: inline-block; width: 42px; height: 42px; align-self: flex-start; flex: none; }

  .lead { position: absolute; left: 0; width: 1000px; top: 500px; text-align: center; }
  .lead h2 { font-weight: 900; font-size: 40px; color: var(--red); line-height: 1.1; }
  .lead p { font-weight: 700; color: var(--teal-dark); font-size: 25px; line-height: 1.32; }
  .lead p.wide { font-size: 26px; }

  .band { position: absolute; left: 0; width: 1000px; background: var(--band); }
  .band.enter { top: 686px; height: 100px; }
  .band.route { top: 806px; height: 244px; }
  .tab {
    position: absolute; height: 22px; background: var(--tab); color: var(--white);
    font-size: 14px; font-weight: 900; text-align: center; line-height: 22px; letter-spacing: 1px;
  }
  .tab.enter { left: 412px; top: 668px; width: 204px; }
  .tab.route { left: 415px; top: 787px; width: 204px; }

  .price { position: absolute; text-align: center; font-size: 13px; font-weight: 700; line-height: 1.3; }
  .price .amount { display: block; color: var(--red); font-size: 13px; }
  .price.deposit { left: 10px; top: 703px; width: 400px; }
  .price.extra { left: 30px; top: 743px; width: 360px; }
  .price.full { left: 600px; top: 703px; width: 400px; }
  .price.tent { left: 620px; top: 743px; width: 360px; }

  .day { position: absolute; font-size: 9.5px; font-weight: 700; line-height: 1.33; width: 335px; }
  .day h3 { color: var(--red); font-size: 11px; font-weight: 900; }
  .day.d0 { left: 18px; top: 830px; }
  .day.d1 { left: 18px; top: 940px; }
  .day.d2 { left: 630px; top: 828px; width: 345px; }
  .day.d3 { left: 626px; top: 892px; width: 360px; }
  .day.d4 { left: 626px; top: 942px; width: 360px; }

  .cta { position: absolute; left: 0; width: 1000px; top: 1052px; text-align: center; font-weight: 900; font-size: 21px; line-height: 1.08; }
  .cta .ask { color: var(--red); display: block; }

  .footer { position: absolute; left: 0; top: 1124px; width: 1000px; height: 76px; background: var(--footer); color: var(--white); }
  .footer .label { position: absolute; left: 170px; top: 14px; width: 100px; text-align: center; font-size: 17px; font-weight: 900; line-height: 1.05; }
  .link { position: absolute; display: flex; align-items: center; gap: 8px; font-size: 15px; font-weight: 900; letter-spacing: 0.5px; white-space: nowrap; }
  .link .sq { width: 16px; height: 16px; border-radius: 50%; background: var(--teal-light); flex: none; }
  .link.l1 { left: 272px; top: 6px; }
  .link.l2 { left: 702px; top: 6px; }
  .link.l3 { left: 342px; top: 29px; }
  .link.l4 { left: 286px; top: 52px; }
  .link.l5 { left: 700px; top: 52px; }
</style>
</head>
<body>
<main class="poster">
  <svg class="road" viewBox="0 0 1000 1200" role="img" aria-label="Tyre-tracked road sweeping from the top left to the bottom right of the poster">
    <defs>
      <linearGradient id="roadTone" x1="0" y1="0" x2="1" y2="1">
        <stop offset="0" stop-color="#2e3436"/>
        <stop offset="0.45" stop-color="#8fa0a6" stop-opacity="0.55"/>
        <stop offset="1" stop-color="#36b0cc"/>
      </linearGradient>
    </defs>
    <path d="M0 262 C 180 300 360 520 470 760 C 540 900 560 1020 600 1124 L1000 1124 L1000 1010 C 820 940 620 700 420 520 C 280 400 140 330 0 305 Z" fill="url(#roadTone)" opacity="0.7"/>
  </svg>

  <div class="brand-mark"><span class="dot"></span><span class="name">7TrekZ</span></div>
  <h1 class="title">7TrekZ 2019</h1>

  <p class="stats">3 Countries | 4 Days | 80 Cars | 1 event</p>
  <p class="countries">
    <span class="word">ENGLAND</span>
    <svg class="flag" width="42" height="42" viewBox="0 0 44 44" aria-hidden="true"><circle cx="22" cy="22" r="21" fill="#ffffff" stroke="#c9cfd2" stroke-width="1"/><rect x="18" y="2" width="8" height="40" fill="#d5161e"/><rect x="2" y="18" width="40" height="8" fill="#d5161e"/></svg>
    <span class="word">· WALES</span>
    <svg class="flag" width="42" height="42" viewBox="0 0 44 44" aria-hidden="true"><path d="M1 22 A21 21 0 0 1 43 22 Z" fill="#ffffff"/><path d="M1 22 A21 21 0 0 0 43 22 Z" fill="#1e8a3e"/><circle cx="22" cy="22" r="21" fill="none" stroke="#c9cfd2" stroke-width="1"/></svg>
    <span class="word">· SCOTLAND</span>
    <svg class="flag" width="42" height="42" viewBox="0 0 44 44" aria-hidden="true"><circle cx="22" cy="22" r="21" fill="#1f5fb4"/><path d="M7 7 L37 37 M37 7 L7 37" stroke="#ffffff" stroke-width="6"/><circle cx="22" cy="22" r="21" fill="none" stroke="#c9cfd2" stroke-width="1"/></svg>
  </p>

  <section class="lead">
    <h2>We drive through 3 countries</h2>
    <p>starting in London</p>
    <p class="wide">travelling through Wales, the lakes and into Scotland</p>
    <p>finishing in Edinburgh.</p>
  </section>

  <div class="band enter"></div>
  <div class="tab enter">ENTER</div>
  <div class="price deposit">- 7TrekZ 2019 Entry Deposit for Two (2) Participants<span class="amount">25.00 £</span></div>
  <div class="price extra">- Extra Participant<span class="amount">65.00 £</span></div>
  <div class="price full">- 7TrekZ 2019 Full-Entry - No Deposit Required<span class="amount">285.00 £</span></div>
  <div class="price tent">- Extra Two-Man Pop-Up Tent<span class="amount">25.00 £</span></div>

  <div class="band route"></div>
  <div class="tab route">Route</div>

  <article class="day d0"><h3>Day 0 - 26th June 2019 [Wed]</h3>A meet up in London for pre-7TrekZ drinks and food. Not compulsory in any way, just an option for those that want a bit of extra socialising and to end the wait! Those wanting to drink and stay local would require accommodation and parking.</article>
  <article class="day d1"><h3>Day 1 - 27th June 2019 [Thur]</h3>Registration. Cars start from the Ridgeway Diner London, arriving between 7 to 8am. We officially start the event by crossing the start line and drive West, driving towards and through Wales, then heading North, tackling many well-known routes and roads and through to where we spend our first night at Camp7TrekZ Wales!</article>
  <article class="day d2"><h3>Day 2 - 28th June 2019 [Fri]</h3>Starting from Camp7TrekZ Wales, we drive North towards and through the Lake District and North into Scotland. We meet up at Camp7TrekZ South-Scotland!</article>
  <article class="day d3"><h3>Day 3 - 29th June 2019 [Sat]</h3>Leaving from Camp7TrekZ South-Scotland, we head further North along the West coast of Scotland where we spend the night at Camp7TrekZ NW-Coast.</article>
  <article class="day d4"><h3>Day 4 - 30th June 2019 [Sun]</h3>Waking up and leaving Camp7TrekZ North-West Coast, we head towards the finish line in Edinburgh. There will be a parade along the way and we finish with a party in a central location. Participants can either stay locally for another night (at cost) or start heading back home for work the next day. Hardcore. (Especially if you live on the South Coast - We salute you!)</article>

  <section class="cta">Want to join our event and be part<br>of the atmosphere?<span class="ask">Why wouldn't you?</span></section>

  <footer class="footer">
    <div class="label">For<br>more<br>info</div>
    <span class="link l1"><span class="sq"></span>https://chatterline.com/7trekz</span>
    <span class="link l2"><span class="sq"></span>info@7trekz.com</span>
    <span class="link l3"><span class="sq"></span>https://snapgrid.com/7trekz</span>
    <span class="link l4"><span class="sq"></span>www.friendwall.com/7trekz</span>
    <span class="link l5"><span class="sq"></span>www.7trekz.com</span>
  </footer>
</main>
</body>
</html>
```